BOLD & MINIMALIST DESIGN NEEDED

We want a very bold but minimalistic business card design that is impactful and utilizes both sides of the business card. Our current logo is included for your use.

We want bold fonts and good use of negative space. We don't want the logo to overpower the design.

Target Market(s)

Professionals who are building new commercial buildings.

Industry/Entity Type

Construction

Contact Information for Business Card

Name, Title, email, office phone, cell phone, website

Font styles to use
Serif
Sans Serif

Requirements
Must have
• Bold design!

```html
<!DOCTYPE html>
<html lang="en">
<head>
<meta charset="utf-8">
<title>Ridgeline Design + Build – Business Card</title>
<link href="https://fonts.googleapis.com/css2?family=Montserrat:wght@400;500;800&display=swap" rel="stylesheet">
<style>
  :root {
    --stage: #d6d6d6;
    --card: #f2f2f2;
    --ink: #141414;
    --green: #6ab42d;
    --green-dark: #4f8f1e;
  }
  * { margin: 0; padding: 0; box-sizing: border-box; }
  html, body {
    width: 1200px; height: 900px; overflow: hidden;
    background: var(--stage);
    font-family: "Montserrat", sans-serif;
    color: var(--ink);
  }
  .stage {
    width: 1200px; height: 900px;
    display: flex; align-items: center; justify-content: center; gap: 40px;
  }
  .card {
    position: relative;
    width: 540px; height: 310px;
    background: var(--card);
    overflow: hidden;
  }

  /* brand name set as text */
  .brand {
    display: flex; align-items: center; gap: 12px;
    font-weight: 800; text-transform: uppercase; color: var(--ink);
  }
  .brand-square { background: var(--green); flex: none; }

  /* front */
  .card-front { display: flex; align-items: center; justify-content: center; }
  .card-front .brand { font-size: 24px; letter-spacing: 1px; }
  .card-front .brand-square { width: 22px; height: 22px; }

  /* back */
  .accent-block {
    position: absolute; right: -60px; bottom: -40px;
    width: 200px; height: 220px;
    background: var(--green);
  }
  .person {
    position: absolute; left: 250px; top: 34px;
  }
  .person-name { font-size: 22px; font-weight: 500; letter-spacing: 0.5px; text-transform: uppercase; }
  .person-title { font-size: 15px; font-weight: 500; color: var(--green); margin-top: 2px; }

  .card-back .brand {
    position: absolute; left: 36px; top: 120px;
    font-size: 13px; gap: 8px; letter-spacing: 0.5px;
  }
  .card-back .brand-square { width: 12px; height: 12px; }

  .contacts {
    position: absolute; left: 36px; bottom: 30px;
    list-style: none; font-size: 12.5px; line-height: 1;
  }
  .contacts li { display: flex; align-items: center; gap: 8px; margin-top: 10px; }
  .contacts .row { display: flex; gap: 22px; }
  .contacts .row span { display: flex; align-items: center; gap: 8px; }
  .icon { width: 13px; height: 13px; fill: var(--green); flex: none; }
</style>
</head>
<body>
<main class="stage">

  <section class="card card-front" aria-label="Card front">
    <div class="brand"><span class="brand-square"></span>Ridgeline Design + Build</div>
  </section>

  <section class="card card-back" aria-label="Card back">
    <div class="accent-block"></div>

    <div class="person">
      <p class="person-name">Daren Velko</p>
      <p class="person-title">CEO</p>
    </div>

    <div class="brand"><span class="brand-square"></span>Ridgeline Design + Build</div>

    <ul class="contacts">
      <li class="row">
        <span>
          <svg class="icon" viewBox="0 0 16 16"><path d="M3 1h3l1.5 4-2 1.3a9 9 0 0 0 4.2 4.2L11 8.5l4 1.5v3a2 2 0 0 1-2 2A12 12 0 0 1 1 3a2 2 0 0 1 2-2z"/></svg>
          555 014 220
        </span>
        <span>
          <svg class="icon" viewBox="0 0 16 16"><rect x="4" y="1" width="8" height="14" rx="1.5"/><rect x="5.5" y="3" width="5" height="8" fill="#f2f2f2"/></svg>
          555 014 221
        </span>
      </li>
      <li>
        <svg class="icon" viewBox="0 0 16 16"><path d="M1 3h14v10H1z"/><path d="M1 3l7 6 7-6" fill="none" stroke="#f2f2f2" stroke-width="1.4"/></svg>
        info@ridgelinebuild.com
      </li>
      <li>
        <svg class="icon" viewBox="0 0 16 16"><circle cx="8" cy="8" r="7"/><path d="M1 8h14M8 1c-3 3-3 11 0 14M8 1c3 3 3 11 0 14" fill="none" stroke="#f2f2f2" stroke-width="1.1"/></svg>
        www.ridgelinebuild.com
      </li>
    </ul>
  </section>

</main>
</body>
</html>
```